Steadfast Care - Need Stationary Design

We need a stationary pack for our new Care company based in the uk
Are corporate colours are Pink and purple
Please use attached logo
Target Market(s)
The Care Industry
Industry/Entity Type
It Company
Contact Information for Business Card
Melissa Rowden
Director

```html
<!DOCTYPE html>
<html lang="en">
<head>
<meta charset="utf-8">
<title>Steadfast Care – Business Cards</title>
<link rel="stylesheet" href="https://fonts.googleapis.com/css2?family=Caveat:wght@600;700&family=Open+Sans:wght@400;600&display=swap">
<style>
  :root {
    --backdrop: #bdae8f;
    --purple-deep: #3a1a63;
    --purple: #5b2d8c;
    --purple-light: #7a4bab;
    --magenta: #c8235e;
    --pink-soft: #e98fb0;
    --frost: #eef0f2;
    --frost-shade: #c9ccd1;
    --text-light: #f3eefa;
    --text-muted: #ddd2ee;
  }
  * { margin: 0; padding: 0; box-sizing: border-box; }
  html, body { width: 736px; height: 1200px; overflow: hidden; }
  body {
    background: var(--backdrop);
    font-family: "Open Sans", Arial, sans-serif;
    position: relative;
  }
  .business-card {
    position: absolute;
    left: 81px;
    width: 578px;
    height: 328px;
    border-radius: 12px;
    overflow: hidden;
    box-shadow: 0 6px 14px rgba(60, 45, 20, 0.22);
    background: linear-gradient(135deg, var(--frost) 0%, #ffffff 45%, var(--frost-shade) 100%);
  }
  .card-one { top: 61px; }
  .card-two { top: 447px; }
  .card-three { top: 834px; }
  .card-art { position: absolute; inset: 0; width: 100%; height: 100%; }
  .card-details {
    position: absolute;
    left: 24px;
    top: 34px;
    color: var(--text-light);
  }
  .person-name {
    font-family: "Caveat", cursive;
    font-weight: 700;
    font-size: 30px;
    line-height: 1;
  }
  .person-role {
    font-family: "Caveat", cursive;
    font-weight: 600;
    font-size: 18px;
    margin-top: 4px;
    color: var(--text-muted);
  }
  .address {
    margin-top: 30px;
    font-size: 14px;
    line-height: 24px;
  }
  .contact-list {
    list-style: none;
    margin-top: 12px;
    font-size: 14px;
    line-height: 24px;
  }
  .contact-list li { display: flex; align-items: center; gap: 8px; }
  .contact-list svg { width: 13px; height: 13px; fill: var(--text-light); flex: none; }
  .brand {
    position: absolute;
    left: 350px;
    top: 70px;
    width: 210px;
    display: flex;
    flex-direction: column;
    align-items: center;
    gap: 16px;
  }
  .brand-dot {
    width: 70px;
    height: 70px;
    border-radius: 50%;
    background: var(--purple);
  }
  .brand-name {
    font-family: "Open Sans", Arial, sans-serif;
    font-weight: 600;
    font-size: 25px;
    color: var(--purple-deep);
    white-space: nowrap;
  }
</style>
</head>
<body>

<svg width="0" height="0" style="position:absolute">
  <defs>
    <linearGradient id="purple-panel" x1="0" y1="0" x2="1" y2="1">
      <stop offset="0" stop-color="#6a3a9c"/>
      <stop offset="0.55" stop-color="#4a2379"/>
      <stop offset="1" stop-color="#341459"/>
    </linearGradient>
    <symbol id="card-background" viewBox="0 0 578 328">
      <path d="M0 0 H350 C328 90 300 150 318 230 C326 270 334 300 328 328 H0 Z" fill="url(#purple-panel)"/>
      <path d="M356 0 C334 90 306 150 324 230 C332 270 340 300 334 328" fill="none" stroke="#c8235e" stroke-width="9"/>
      <path d="M366 0 C344 90 316 150 334 230 C342 270 350 300 344 328" fill="none" stroke="#e98fb0" stroke-width="3"/>
    </symbol>
    <symbol id="icon-phone" viewBox="0 0 24 24"><path d="M6.6 10.8a15.1 15.1 0 0 0 6.6 6.6l2.2-2.2c.3-.3.7-.4 1-.2 1.1.4 2.3.6 3.6.6.6 0 1 .4 1 1V20c0 .6-.4 1-1 1A17 17 0 0 1 3 4c0-.6.4-1 1-1h3.5c.6 0 1 .4 1 1 0 1.3.2 2.5.6 3.6.1.3 0 .7-.2 1z"/></symbol>
    <symbol id="icon-mail" viewBox="0 0 24 24"><path d="M2 5h20v14H2z M3.5 6.5 12 12.5l8.5-6z" fill-rule="evenodd"/></symbol>
    <symbol id="icon-web" viewBox="0 0 24 24"><path d="M12 2a10 10 0 1 0 0 20 10 10 0 0 0 0-20zm0 2c1.2 1.4 2 3.6 2.2 7H9.8C10 7.6 10.8 5.4 12 4zM4.1 13h3.7c.1 2.3.6 4.3 1.4 5.6A8 8 0 0 1 4.1 13zm0-2a8 8 0 0 1 5.1-5.6c-.8 1.3-1.3 3.3-1.4 5.6zm5.7 2h4.4c-.2 3.4-1 5.6-2.2 7-1.2-1.4-2-3.6-2.2-7zm5 5.6c.8-1.3 1.3-3.3 1.4-5.6h3.7a8 8 0 0 1-5.1 5.6zm1.4-7.6c-.1-2.3-.6-4.3-1.4-5.6a8 8 0 0 1 5.1 5.6z"/></symbol>
  </defs>
</svg>

<article class="business-card card-one">
  <svg class="card-art" aria-hidden="true"><use href="#card-background"/></svg>
  <div class="card-details">
    <h1 class="person-name">Melissa Rowden</h1>
    <p class="person-role">Placement &amp; Resources Director</p>
    <p class="address">4 Alder Court<br>18 Mill Lane<br>Kingsbridge Devon TQ7 1AB</p>
    <ul class="contact-list">
      <li><svg><use href="#icon-phone"/></svg>0203 555 0142</li>
      <li><svg><use href="#icon-mail"/></svg>Melissarowden@steadfastcare.co.uk</li>
      <li><svg><use href="#icon-web"/></svg>www.steadfastcare.co.uk</li>
    </ul>
  </div>
  <div class="brand"><span class="brand-dot"></span><span class="brand-name">Steadfast Care</span></div>
</article>

<article class="business-card card-two">
  <svg class="card-art" aria-hidden="true"><use href="#card-background"/></svg>
  <div class="card-details">
    <h1 class="person-name">Joanne Hartley</h1>
    <p class="person-role">Care Director</p>
    <p class="address">4 Alder Court<br>18 Mill Lane<br>Kingsbridge Devon TQ7 1AB</p>
    <ul class="contact-list">
      <li><svg><use href="#icon-phone"/></svg>07700900123</li>
      <li><svg><use href="#icon-mail"/></svg>Joannehartley@steadfastcare.co.uk</li>
      <li><svg><use href="#icon-web"/></svg>www.steadfastcare.co.uk</li>
    </ul>
  </div>
  <div class="brand"><span class="brand-dot"></span><span class="brand-name">Steadfast Care</span></div>
</article>

<article class="business-card card-three">
  <svg class="card-art" aria-hidden="true"><use href="#card-background"/></svg>
  <div class="card-details">
    <h1 class="person-name">Daniel Ashcroft</h1>
    <p class="person-role">Business Development Manager</p>
    <p class="address">4 Alder Court<br>18 Mill Lane<br>Kingsbridge Devon TQ7 1AB</p>
    <ul class="contact-list">
      <li><svg><use href="#icon-phone"/></svg>07700900456</li>
      <li><svg><use href="#icon-mail"/></svg>daniel@steadfastcare.co.uk</li>
      <li><svg><use href="#icon-web"/></svg>www.steadfastcare.co.uk</li>
    </ul>
  </div>
  <div class="brand"><span class="brand-dot"></span><span class="brand-name">Steadfast Care</span></div>
</article>

</body>
</html>
```